QDN Advisory needs business card

Having just developed a logo, I now want to use that logo in the development of a business card. The card should contain the logo, my name, title, phone, email, website and physical address. I would like to use one side of the card for details and the other side for logo and messaging. Use your creativity to place the information effectively. I want the logo to appear in a strong blue, which may be matched on the back side of the card, where the logo might be reversed out in white. I want the text to be in either dark blue or black (not light blue or gray).
I am consultant, primarily helping small and mid-size companies refine their strategy, reorganize their staff and propel forward in their industry. I also teach at universities and coach on a one-on-one basis. The final design should reflect expertise, guidance, judgement, perspective, experience.
The font used in the logo is ACaslonPro.

Target Market(s)

small to mid-size companies in the US seeking business guidance

Industry/Entity Type

Business

Font styles to use
Other font styles liked:
• ACaslonPro

Colors
0455a3
0255a3
3277b5

Requirements
Must have
• Card must convey my name and information clearly. Do not make it too small - many of my customers are 50+ years old. Please use all three of my titles: consultant / coach / instructor.
Should not have
• Please do not use icons to represent the phone, email, web. Do not use p / e / w either to indicate those details.

I have decided that a swatch of color, especially a "blue wave," does not work for me. I would rather have a simpler, more reserved look rather than a very contemporary, high color card.

Please do not deconstruct the logo or put it in a different font or italics.

```html
<!DOCTYPE html>
<html lang="en">
<head>
<meta charset="utf-8">
<title>QDN Advisory — Business Card</title>
<link rel="stylesheet" href="https://fonts.googleapis.com/css2?family=Libre+Caslon+Text:wght@400;700&display=swap">
<style>
  :root {
    --brand-blue: #0455a3;
    --ink: #111111;
    --paper: #ffffff;
    --backdrop: #ecebe7;
    --card-shadow: rgba(0, 0, 0, 0.18);
  }
  * { margin: 0; padding: 0; box-sizing: border-box; }
  html, body {
    width: 1200px;
    height: 857px;
    overflow: hidden;
    background: var(--backdrop);
    font-family: "Libre Caslon Text", "Times New Roman", serif;
  }
  .card-sheet {
    width: 1200px;
    height: 857px;
    display: flex;
    align-items: center;
    justify-content: center;
    gap: 48px;
  }
  .card {
    position: relative;
    width: 520px;
    height: 298px;
    box-shadow: 0 6px 18px var(--card-shadow);
  }

  /* Front: contact details */
  .card--front {
    background: var(--paper);
    color: var(--ink);
  }
  .holder-name {
    position: absolute;
    top: 36px;
    left: 36px;
    font-size: 21px;
    font-weight: 700;
  }
  .contact-list {
    position: absolute;
    left: 36px;
    bottom: 40px;
    list-style: none;
    font-size: 15px;
    line-height: 1.45;
  }
  .front-wordmark {
    position: absolute;
    right: 40px;
    top: 128px;
    font-size: 25px;
    font-weight: 400;
    color: var(--brand-blue);
  }

  /* Back: logo and messaging */
  .card--back {
    background: var(--brand-blue);
    color: var(--paper);
    display: flex;
    flex-direction: column;
    align-items: center;
    justify-content: center;
    gap: 30px;
  }
  .back-wordmark {
    font-size: 40px;
    font-weight: 400;
  }
  .titles {
    font-size: 16px;
    font-weight: 700;
    letter-spacing: 0.02em;
  }
</style>
</head>
<body>
  <main class="card-sheet">
    <section class="card card--front" aria-label="Card front">
      <p class="holder-name">R. Dalton Whitmore, CCIM</p>
      <ul class="contact-list">
        <li>(555) 014-2287</li>
        <li>Dalton@qdn-advisory.com</li>
        <li>www.qdn-advisory.com</li>
        <li>2715 Larkhaven Court</li>
        <li>Maple Ridge, FL 32900</li>
      </ul>
      <p class="front-wordmark">QDN Advisory</p>
    </section>

    <section class="card card--back" aria-label="Card back">
      <p class="back-wordmark">QDN Advisory</p>
      <p class="titles">Consultant - Coach - Instructor</p>
    </section>
  </main>
</body>
</html>
```